Advertisement flyer (editable) and market report template in same style

Advertisement flyer (aka 1 page Media Kit) for us to sell advertising space on our website banner, tidecargomarket.com, and a market report template in the same style.
We would like to use colors that are used on our website. The flyer and market report template should be simple, and professional-looking. It should not look "old" or "boring". I've attached two drafts (1 each respectively), and our logo.

Target Market(s)

30-60 year old men but should look cool, new-aged, and fresh.

Industry/Entity Type

Shipping

Font styles to use
Serif

Requirements
Must have
• Editable layout so we can adjust text, numbers, and graphics on all. A fresh and new look. Colors per www.TideCargoMarket.com website.
Should not have
• Boring layout and font

```html
<!DOCTYPE html>
<html lang="en">
<head>
<meta charset="utf-8">
<title>TideCargoMarket Weekly Market Report</title>
<link rel="stylesheet" href="https://fonts.googleapis.com/css2?family=Questrial&display=swap">
<style>
:root{
  --band-grey:#e3e4e6;
  --panel-grey:#e9ebee;
  --sky:#5dc9f2;
  --ocean:#2aa3d6;
  --pale:#e4f1fa;
  --navy:#27476f;
  --date-blue:#4b7db8;
  --ink:#1f2a36;
  --up:#2ea03a;
  --down:#e0281e;
}
*{box-sizing:border-box;margin:0;padding:0}
html,body{width:1200px;height:3226px;overflow:hidden}
body{position:relative;background:#fff;font-family:"Questrial",sans-serif;color:var(--ink)}
.abs{position:absolute}

.masthead{left:0;top:0;width:1200px;height:226px;background:var(--band-grey)}
.brand{left:80px;top:62px;display:flex;align-items:center;gap:16px}
.brand-dot{width:40px;height:40px;border-radius:50%;background:var(--ocean)}
.brand-name{font-size:36px;color:var(--navy)}
.issue-date{left:80px;top:172px;font-size:34px;color:var(--date-blue)}

.report-title{left:673px;top:232px;width:482px;text-align:center;font-size:38px;line-height:44px;color:var(--navy)}

.panel{left:673px;width:482px;background:var(--panel-grey);padding:22px 40px;font-size:22px;line-height:25px}
.panel p{text-align:justify;margin-bottom:10px}
.panel .gap{margin-top:62px}
.accent{left:673px;width:482px;background:var(--sky)}

.section-title{left:43px;width:596px;text-align:center;font-size:42px;color:var(--navy)}

.rate-table{left:43px;width:596px;font-size:21px}
.rate-table .head{background:var(--sky);color:#fff;height:97px;position:relative}
.rate-table .head .caption{position:absolute;top:6px;left:172px;right:0;text-align:center;font-size:30px}
.rate-table .row{display:grid;grid-template-columns:172px 172px 140px 75px 37px;align-items:center}
.rate-table.wide .row{grid-template-columns:226px 140px 130px 63px 37px}
.rate-table .head .row{position:absolute;left:0;right:0;top:50px;height:44px}
.rate-table .head .row span{text-align:center}
.rate-table .head .row .wow{font-size:18px;line-height:19px}
.rate-table .body .row{height:54px;border-top:2px solid #fff}
.rate-table .body .row>span{height:100%;display:flex;align-items:center;justify-content:center}
.rate-table .body .label{background:var(--ocean);color:#fff;justify-content:flex-start!important;padding-left:20px;line-height:22px}
.rate-table .body .row:nth-child(odd)>span:not(.label){background:var(--pale)}
.rate-table .body .row:nth-child(even)>span:not(.label){background:var(--sky);color:#fff}
.arrow{width:16px;height:22px}

.trend-chart{left:43px;top:1505px}

.handy-title{left:0;top:2318px;width:1200px;text-align:center;font-size:64px;color:var(--navy)}
.handy-band{left:0;top:2408px;width:1200px;height:344px;background:var(--band-grey)}
.handy-box{left:43px;top:2447px;width:1112px;height:256px;border-radius:16px;background:#f5f7f9;border:1px solid #cfd3d8}

.bunker-title{left:43px;top:2786px;width:516px;text-align:center;font-size:64px;color:var(--navy)}
.footer-band{left:0;top:3160px;width:1200px;height:66px;background:var(--band-grey)}
</style>
</head>
<body>

<header class="abs masthead"></header>
<div class="abs brand"><span class="brand-dot"></span><span class="brand-name">TideCargoMarket</span></div>
<div class="abs issue-date">September 28, 2016</div>

<h1 class="abs report-title">TCM Weekly<br>Search Marketing Report</h1>

<!-- commentary panels -->
<div class="abs panel" style="top:333px;height:273px">
  <p>Assignments ask for a ‘report’, rather than an essay, and students are often confused about what that really means.</p>
  <p>Likewise, in business, confronted with a request for a ‘report’ to a senior manager, many people struggle to know what to write.</p>
  <p>Confusion often arises about the writing</p>
</div>
<div class="abs accent" style="top:606px;height:114px"></div>
<div class="abs panel" style="top:720px;height:258px">
  <p>Assignments ask for a ‘report’, rather than an essay, and students are often confused about what that really means.</p>
  <p>Likewise, in business, confronted with a request for a ‘report’ to a senior manager, many people struggle to know what to write.</p>
  <p>Confusion often arises about the writing</p>
</div>
<div class="abs accent" style="top:978px;height:119px"></div>
<div class="abs panel" style="top:1097px;height:731px">
  <p>Assignments ask for a ‘report’, rather than an essay, and students are often confused about what that really means.</p>
  <p>Likewise, in business, confronted with a request for a ‘report’ to a senior manager, many people struggle to know what to write.</p>
  <p>Confusion often arises about the writing style, what to include, the factors.</p>
  <p class="gap">Assignments ask for a ‘report’, rather than an essay, and students are often confused about what that really means.</p>
  <p>Likewise, in business, confronted with a request for a ‘report’ to a senior manager, many people struggle to know what to write.</p>
  <p>Confusion often arises about the writing style, what to include, the factors.</p>
</div>
<div class="abs accent" style="top:1828px;height:118px"></div>
<div class="abs panel" style="top:1946px;height:322px">
  <p>Assignments ask for a ‘report’, rather than an essay, and students are often confused about what that really means.</p>
  <p>Likewise, in business, confronted with a request for a ‘report’ to a senior manager, many people struggle to know what to write.</p>
  <p>Confusion often arises about the writing style, what to include, the factors.</p>
</div>

<svg width="0" height="0" style="position:absolute">
  <defs>
    <symbol id="up" viewBox="0 0 16 22"><path d="M8 0 16 10H11V22H5V10H0Z" fill="#2ea03a"/></symbol>
    <symbol id="down" viewBox="0 0 16 22"><path d="M8 22 16 12H11V0H5V12H0Z" fill="#e0281e"/></symbol>
  </defs>
</svg>

<!-- Crude -->
<h2 class="abs section-title" style="top:268px">Crude Prices</h2>
<div class="abs rate-table" style="top:344px">
  <div class="head"><div class="caption">Crude Prices</div>
    <div class="row"><span>$/bbl</span><span>22- Sep</span><span>15-Sep</span><span class="wow" style="grid-column:span 2">W-O-W<br>Change</span></div></div>
  <div class="body">
    <div class="row"><span class="label">ICE Brent</span><span>47.29</span><span>46.30</span><span>0.99</span><span><svg class="arrow"><use href="#up"/></svg></span></div>
    <div class="row"><span class="label">Dtd Brent</span><span>47.29</span><span>46.30</span><span>0.99</span><span><svg class="arrow"><use href="#up"/></svg></span></div>
    <div class="row"><span class="label">Dubai</span><span>44.71</span><span>42.86</span><span>1.85</span><span><svg class="arrow"><use href="#up"/></svg></span></div>
  </div>
</div>

<!-- Products -->
<h2 class="abs section-title" style="top:646px">Products</h2>
<div class="abs rate-table" style="top:720px">
  <div class="head"><div class="caption">Products</div>
    <div class="row"><span>$/bbl</span><span>22- Sep</span><span>15-Sep</span><span class="wow" style="grid-column:span 2">W-O-W<br>Change</span></div></div>
  <div class="body">
    <div class="row"><span class="label">ICE Brent</span><span>47.29</span><span>46.30</span><span>0.99</span><span><svg class="arrow"><use href="#up"/></svg></span></div>
    <div class="row"><span class="label">Dtd Brent</span><span>47.29</span><span>46.30</span><span>0.99</span><span><svg class="arrow"><use href="#up"/></svg></span></div>
    <div class="row"><span class="label">Dubai</span><span>44.71</span><span>42.86</span><span>1.85</span><span><svg class="arrow"><use href="#up"/></svg></span></div>
  </div>
</div>

<!-- VLCC -->
<h2 class="abs section-title" style="top:1022px">VLCC</h2>
<div class="abs rate-table" style="top:1101px">
  <div class="head"><div class="caption">Spot VLCC Rates</div>
    <div class="row"><span>$/bbl</span><span>22- Sep</span><span>15-Sep</span><span class="wow" style="grid-column:span 2">W-O-W<br>Change</span></div></div>
  <div class="body">
    <div class="row"><span class="label">AG/USGC</span><span>25.00</span><span>22.00</span><span>3.00</span><span><svg class="arrow"><use href="#up"/></svg></span></div>
    <div class="row"><span class="label">AG/Japan</span><span>38.00</span><span>32.00</span><span>6.00</span><span><svg class="arrow"><use href="#up"/></svg></span></div>
    <div class="row"><span class="label">AG/Singapore</span><span>39.00</span><span>33.00</span><span>6.00</span><span><svg class="arrow"><use href="#up"/></svg></span></div>
    <div class="row"><span class="label">WAF/USGC</span><span>42.50</span><span>45.00</span><span>-2.50</span><span><svg class="arrow"><use href="#down"/></svg></span></div>
    <div class="row"><span class="label">WAF/Far East</span><span>48.50</span><span>42.50</span><span>6.00</span><span><svg class="arrow"><use href="#up"/></svg></span></div>
  </div>
</div>

<svg class="abs trend-chart" width="452" height="312" viewBox="0 0 452 312" font-family="Questrial, sans-serif" font-size="17" fill="#333">
  <g stroke="#999" stroke-width="1.5">
    <line x1="66" y1="250" x2="444" y2="250"/>
  </g>
  <g text-anchor="end">
    <text x="50" y="256">0.0</text><text x="50" y="229">0.5</text><text x="50" y="203">1.0</text>
    <text x="50" y="176">1.5</text><text x="50" y="149">2.0</text><text x="50" y="123">2.5</text>
    <text x="50" y="96">3.0</text><text x="50" y="69">3.5</text><text x="50" y="43">4.0</text>
    <text x="50" y="16">4.5</text>
  </g>
  <g text-anchor="end">
    <text transform="translate(78 264) rotate(-45)">Jan-15</text>
    <text transform="translate(124 264) rotate(-45)">Apr-15</text>
    <text transform="translate(170 264) rotate(-45)">Jul-15</text>
    <text transform="translate(216 264) rotate(-45)">Oct-15</text>
    <text transform="translate(262 264) rotate(-45)">Jan-16</text>
    <text transform="translate(308 264) rotate(-45)">Apr-16</text>
    <text transform="translate(354 264) rotate(-45)">Jul-16</text>
  </g>
  <polyline fill="none" stroke="#2a5573" stroke-width="5" stroke-linejoin="round"
    points="70,181 81,197 92,175 104,186 115,165 126,143 137,117 148,133 160,101 171,90 182,111 193,42 204,53 216,79 227,143 238,101 249,170 260,159 272,181 283,165 294,149 305,186 316,159 328,175 339,191 350,170 361,186 372,197 384,191 395,207 406,218 417,213 428,223 440,202"/>
</svg>

<!-- MR/LR -->
<h2 class="abs section-title" style="top:1876px">MR/LR</h2>
<div class="abs rate-table wide" style="top:1950px">
  <div class="head"><div class="caption">Spot MR/LR Rates</div>
    <div class="row"><span>WS</span><span>22- Sep</span><span>15-Sep</span><span class="wow" style="grid-column:span 2">W-O-W<br>Change</span></div></div>
  <div class="body">
    <div class="row"><span class="label">AG/Japan (75 kt)</span><span>55.00</span><span>67.50</span><span>3.00</span><span><svg class="arrow"><use href="#down"/></svg></span></div>
    <div class="row"><span class="label">AG/Japan (55 kt)</span><span>80.00</span><span>82.50</span><span>6.00</span><span><svg class="arrow"><use href="#down"/></svg></span></div>
    <div class="row"><span class="label">AG/Japan (30 kt)</span><span>100.00</span><span>92.50</span><span>6.00</span><span><svg class="arrow"><use href="#up"/></svg></span></div>
    <div class="row"><span class="label">Singapore/Japan (30 kt)</span><span>117.00</span><span>117.50</span><span>-2.50</span><span><svg class="arrow"><use href="#down"/></svg></span></div>
  </div>
</div>

<!-- Handy -->
<h2 class="abs handy-title">Handy</h2>
<div class="abs handy-band"></div>
<div class="abs handy-box"></div>

<!-- Bunker -->
<h2 class="abs bunker-title">Bunker</h2>
<div class="abs accent" style="top:2752px;height:129px"></div>
<div class="abs panel" style="top:2881px;height:248px"></div>
<div class="abs rate-table" style="top:2870px">
  <div class="head"><div class="caption">Bunker Prices</div>
    <div class="row"><span>$/T</span><span>22- Sep</span><span>15-Sep</span><span class="wow" style="grid-column:span 2">W-O-W<br>Change</span></div></div>
  <div class="body">
    <div class="row"><span class="label">Singapore 380 cst</span><span>255.00</span><span>258.00</span><span>-3.00</span><span><svg class="arrow"><use href="#down"/></svg></span></div>
    <div class="row"><span class="label">Singapore 180 cst</span><span>266.00</span><span>271.00</span><span>-5.00</span><span><svg class="arrow"><use href="#down"/></svg></span></div>
    <div class="row"><span class="label">Gasoil</span><span>412.00</span><span>415.00</span><span>-3.00</span><span><svg class="arrow"><use href="#down"/></svg></span></div>
  </div>
</div>

<footer class="abs footer-band"></footer>
</body>
</html>
```